Lanterne architecture business cards

We are a new company based in New Zealand. We Specialize in High end Luxury Residential Architecture.

Every home is bespoke and is designed to each clients individual requirements and needs.

I like to design buildings that inspire people through light and form while offering a high level of comfort and usability.

Lines of sight, proportion and balance are fundamental to the spaces I create.
Updates

August 5th is current deadline - Today's date is the 13th of August.

Target Market(s)

New Zealanders who want a custom individual home design, typically 30-65 year old males and females

Industry/Entity Type

Architecture

Contact Information for Business Card

Director - Derek Tolson
Contact Number - 0279164073
Email - info@lanternearchitecture-example.co.nz
Webstie - www.lanternearchitecture-example.co.nz
Social Media - @lanternearchitecture

Font styles to use
Sans Serif

Requirements
Must have
• Logo (Both Sides)
Website
Email
Contact Number
Social Media

Nice to have
• Texture
Should not have
• More than 3 colours - typically I would've thought 2 would be good to match the logo.

```html
<!DOCTYPE html>
<html lang="en">
<head>
<meta charset="utf-8">
<title>Lanterne Architecture – Business Cards</title>
<link rel="stylesheet" href="https://fonts.googleapis.com/css2?family=Lato:wght@400;700&display=swap">
<style>
  :root {
    --backdrop: #d7d7d7;
    --paper: #ffffff;
    --ink: #06070a;
    --ink-soft: #1e232b;
    --muted: #6b6b6b;
    --reverse: #ffffff;
  }
  * { box-sizing: border-box; margin: 0; padding: 0; }
  html, body {
    width: 1200px;
    height: 1143px;
    overflow: hidden;
    background: var(--backdrop);
    font-family: "Lato", sans-serif;
  }
  .card {
    position: absolute;
    left: 299px;
    width: 602px;
    height: 344px;
  }
  .card--front { top: 180px; background: var(--paper); }
  .card--back { top: 621px; background: var(--ink); }

  /* brand lockup */
  .brand {
    position: absolute;
    display: flex;
    flex-direction: column;
    align-items: center;
    font-weight: 400;
    text-transform: uppercase;
  }
  .brand__mark {
    border-radius: 50%;
    border-style: solid;
  }
  .brand__name { line-height: 1; }
  .brand__sub { line-height: 1; }

  .card--front .brand {
    left: 40px;
    width: 200px;
    top: 126px;
    color: var(--ink);
  }
  .card--front .brand__mark {
    width: 38px; height: 38px;
    border-width: 4px; border-color: var(--ink);
    margin-bottom: 20px;
  }
  .card--front .brand__name {
    font-size: 17px;
    letter-spacing: 13px;
    margin-right: -13px;
  }
  .card--front .brand__sub {
    font-size: 6px;
    letter-spacing: 10.4px;
    margin-right: -10.4px;
    margin-top: 6px;
  }

  .divider {
    position: absolute;
    left: 266px;
    top: 117px;
    width: 1.5px;
    height: 110px;
    background: var(--ink);
  }

  .contact {
    position: absolute;
    left: 294px;
    top: 108px;
  }
  .contact__name {
    font-weight: 700;
    font-size: 26px;
    color: var(--ink-soft);
    line-height: 1;
  }
  .contact__role {
    font-size: 15px;
    color: var(--muted);
    margin-top: 6px;
    line-height: 1;
  }
  .contact__list {
    list-style: none;
    margin-top: 16px;
  }
  .contact__item {
    display: flex;
    align-items: center;
    height: 20px;
    font-size: 13.5px;
    color: var(--muted);
  }
  .contact__icon {
    width: 14px; height: 14px;
    margin-right: 11px;
    flex: none;
  }

  .social {
    position: absolute;
    left: 0; right: 0;
    top: 283px;
    display: flex;
    justify-content: center;
    align-items: center;
    font-size: 16px;
    color: var(--muted);
  }
  .social__marker {
    width: 12px; height: 12px;
    background: var(--ink);
    border-radius: 2px;
    margin-right: 9px;
  }

  .card--back .brand {
    left: 0; right: 0;
    top: 112px;
    color: var(--reverse);
  }
  .card--back .brand__mark {
    width: 60px; height: 60px;
    border-width: 6px; border-color: var(--reverse);
    margin-bottom: 34px;
  }
  .card--back .brand__name {
    font-size: 26px;
    letter-spacing: 21px;
    margin-right: -21px;
  }
  .card--back .brand__sub {
    font-size: 8px;
    letter-spacing: 17.5px;
    margin-right: -17.5px;
    margin-top: 12px;
  }
</style>
</head>
<body>

<section class="card card--front" aria-label="Business card front">
  <div class="brand">
    <span class="brand__mark" aria-hidden="true"></span>
    <span class="brand__name">Lanterne</span>
    <span class="brand__sub">Architecture</span>
  </div>

  <span class="divider" aria-hidden="true"></span>

  <div class="contact">
    <h1 class="contact__name">Derek Tolson</h1>
    <p class="contact__role">Director</p>
    <ul class="contact__list">
      <li class="contact__item">
        <svg class="contact__icon" viewBox="0 0 24 24" aria-hidden="true">
          <path fill="#06070a" d="M6.6 10.8c1.4 2.8 3.8 5.1 6.6 6.6l2.2-2.2c.3-.3.7-.4 1-.2 1.1.4 2.3.6 3.6.6.6 0 1 .4 1 1V20c0 .6-.4 1-1 1C10.6 21 3 13.4 3 4c0-.6.4-1 1-1h3.5c.6 0 1 .4 1 1 0 1.2.2 2.4.6 3.6.1.3 0 .7-.2 1l-2.3 2.2z"/>
          <path fill="none" stroke="#06070a" stroke-width="1.8" d="M14 2.5a7.5 7.5 0 0 1 7.5 7.5M14 6a4 4 0 0 1 4 4"/>
        </svg>
        0279164073
      </li>
      <li class="contact__item">
        <svg class="contact__icon" viewBox="0 0 24 24" aria-hidden="true">
          <rect x="1" y="4" width="22" height="16" fill="#06070a"/>
          <path d="M1.5 4.5 12 13 22.5 4.5M1.5 19.5 9 11.5M22.5 19.5 15 11.5" fill="none" stroke="#fff" stroke-width="1.6"/>
        </svg>
        info@lanternearchitecture-example.co.nz
      </li>
      <li class="contact__item">
        <svg class="contact__icon" viewBox="0 0 24 24" aria-hidden="true" fill="none" stroke="#06070a" stroke-width="1.6">
          <circle cx="12" cy="12" r="10"/>
          <ellipse cx="12" cy="12" rx="4.5" ry="10"/>
          <path d="M2 12h20M4 7h16M4 17h16M12 2v20"/>
        </svg>
        www.lanternearchitecture-example.co.nz
      </li>
    </ul>
  </div>

  <p class="social"><span class="social__marker" aria-hidden="true"></span>@lanternearchitecture</p>
</section>

<section class="card card--back" aria-label="Business card back">
  <div class="brand">
    <span class="brand__mark" aria-hidden="true"></span>
    <span class="brand__name">Lanterne</span>
    <span class="brand__sub">Architecture</span>
  </div>
</section>

</body>
</html>
```